Business Card Design Project

Black Writing

Torch Vell

Target Market(s)

18 - 80 year olds

Industry/Entity Type

Business

Requirements
Must have
• Clean

```html
<!DOCTYPE html>
<html lang="en">
<head>
<meta charset="UTF-8">
<title>Torch Vell – Business Card</title>
<link rel="stylesheet" href="https://fonts.googleapis.com/css2?family=Cinzel+Decorative:wght@900&family=Arimo:wght@400;700&display=swap">
<style>
  :root {
    --card-black: #000000;
    --gold: #d2ae5a;
    --gold-light: #f5e09a;
    --gold-dark: #7d5e1e;
    --cream: #efe0b0;
    --glow: #c79a4a;
    --glow-warm: #7a2e22;
  }
  html, body {
    margin: 0;
    padding: 0;
    width: 1200px;
    height: 667px;
    overflow: hidden;
    background: var(--card-black);
  }
  .card {
    position: relative;
    width: 1200px;
    height: 667px;
    background: var(--card-black);
  }
  .emblem {
    position: absolute;
    left: 420px;
    top: 72px;
    width: 360px;
    height: 360px;
  }
  .brand-name {
    position: absolute;
    left: 0;
    top: 468px;
    width: 1200px;
    margin: 0;
    text-align: center;
    font-family: "Cinzel Decorative", serif;
    font-weight: 900;
    font-size: 64px;
    line-height: 1;
    letter-spacing: 8px;
    color: var(--gold);
  }
  .service {
    position: absolute;
    left: 0;
    top: 550px;
    width: 1200px;
    margin: 0;
    text-align: center;
    font-family: "Arimo", sans-serif;
    font-weight: 700;
    font-size: 29px;
    line-height: 1.1;
    letter-spacing: 0.5px;
    color: var(--cream);
  }
  .contact {
    position: absolute;
    left: 0;
    top: 587px;
    width: 1200px;
    margin: 0;
    text-align: center;
    font-family: "Arimo", sans-serif;
    font-weight: 400;
    font-size: 22px;
    line-height: 1.1;
    letter-spacing: 0.5px;
    color: var(--cream);
  }
</style>
</head>
<body>
  <main class="card">
    <svg class="emblem" viewBox="0 0 360 360" role="img" aria-label="Gold Egyptian eye illustration with a glowing pupil inside the ring">
      <defs>
        <linearGradient id="ringGold" x1="0" y1="0" x2="0" y2="1">
          <stop offset="0" stop-color="var(--gold-light)"/>
          <stop offset="0.5" stop-color="var(--gold)"/>
          <stop offset="1" stop-color="var(--gold-dark)"/>
        </linearGradient>
        <radialGradient id="emblemFill" cx="0.5" cy="0.42" r="0.55">
          <stop offset="0" stop-color="var(--glow)" stop-opacity="0.85"/>
          <stop offset="0.35" stop-color="var(--gold-dark)" stop-opacity="0.55"/>
          <stop offset="0.7" stop-color="var(--glow-warm)" stop-opacity="0.18"/>
          <stop offset="1" stop-color="var(--card-black)"/>
        </radialGradient>
      </defs>
      <circle cx="180" cy="180" r="172" fill="url(#emblemFill)" stroke="url(#ringGold)" stroke-width="12"/>
    </svg>
    <h1 class="brand-name">TORCH VELL</h1>
    <p class="service">PSYCHIC TAROT READING</p>
    <p class="contact">CONTACT: 987 65432100</p>
  </main>
</body>
</html>
```